Premium Honey Fusions need a label design. 5 awesome blends (see below)

We need a label design for a line of honey. Brand is an existing brand called MELVORIN. www.melvorinusa.example
MELVORIN is a line of juices. The honey line is an extension of the MELVORIN juice line.
Blends are:
Honey Cinnamon
Honey Saffron
Honey Ginger
Honey Herbs
Honey Wild Flower
PRODUCT FROM INDIA
We need a label design for a line of honey. Brand is an existing brand called MELVORIN.
See www.melvorinusa.example
We would like to see label designs that:
-are easy to read, clean
-"Honey Cinnamon”, etc... should be prominent, as it will be what will set us apart.
-use colors that communicate "premium honey"
-premium
-unique
-healthy/good for you
-We need a “Help us save the bees” type message on the logo. We will give % of profit from sale of honey to go towards saving the bees.
The final design should communicate :
-healthy
-DELICIOUS!!!! (it is!)
-premium
-unique
-exotic
Glass bottle is square (see pics) and label has 3 sides:
Front panel
Side panel 1: will be nutritional, ingredients, UPC, etc
Side panel 2: a story about bees? about saffron, about cinnamon??
Target Market(s)
Hispanic and American markets.
Healthy conscious people.
Premium honey market
Look and feel

```html
<!DOCTYPE html>
<html lang="en">
<head>
<meta charset="utf-8">
<title>MELVORIN Honey – Front Labels</title>
<link rel="stylesheet" href="https://fonts.googleapis.com/css2?family=Poppins:wght@400;500;700;800&family=Lobster&family=Oswald:wght@500&display=swap">
<style>
  :root {
    --page: #ffffff;
    --label: #ffffff;
    --comb-light: #fff4c9;
    --comb-mid: #ffd45a;
    --comb-deep: #f6b21f;
    --brand-red: #d2141c;
    --honey-orange: #e8770f;
    --ink: #2b1a10;
    --wildflower: #6b2a12;
    --saffron: #6a2e9c;
    --badge-line: #f2a93b;
    --save-red: #e0262b;
    --petal-gold: #f7c860;
    --saffron-red: #9a2a16;
    --saffron-violet: #7a4cc0;
  }
  * { box-sizing: border-box; margin: 0; padding: 0; }
  html, body { width: 1200px; height: 1200px; overflow: hidden; background: var(--page); }
  .canvas {
    position: relative; width: 1200px; height: 1200px;
    display: flex; justify-content: center; align-items: center; gap: 40px;
  }
  .label {
    position: relative; width: 500px; height: 500px;
    background: var(--label);
    box-shadow: 0 0 0 1px #eee;
    overflow: hidden;
    font-family: "Poppins", sans-serif;
  }
  .comb-field {
    position: absolute; left: 60px; top: 0; width: 400px; height: 290px;
    background: radial-gradient(ellipse at 55% 45%, var(--comb-mid) 0%, var(--comb-light) 55%, rgba(255,255,255,0) 78%);
  }
  .brand {
    position: absolute; left: 0; right: 0; top: 48px;
    display: flex; justify-content: center; align-items: center; gap: 12px;
  }
  .brand-dot { width: 18px; height: 18px; border-radius: 50%; background: var(--brand-red); }
  .brand-name {
    font-weight: 800; font-size: 56px; letter-spacing: 1px;
    color: var(--brand-red); line-height: 1;
  }
  .product-word {
    position: absolute; left: 70px; top: 140px;
    font-family: "Lobster", cursive;
    font-size: 130px; line-height: 1; color: var(--honey-orange);
  }
  .descriptor {
    position: absolute; right: 70px; top: 296px; text-align: right;
    color: var(--ink); font-size: 14px; line-height: 1.4; font-weight: 400;
  }
  .variety {
    display: block; font-weight: 700; font-size: 28px; line-height: 1.2;
    letter-spacing: 0.5px; margin-top: 2px;
  }
  .variety--wildflower { color: var(--wildflower); }
  .variety--saffron { color: var(--saffron); }
  .bee-badge {
    position: absolute; left: 0; top: 384px; width: 110px; height: 110px;
  }
  .bee-badge svg { position: absolute; inset: 0; }
  .bee-mark {
    position: absolute; left: 16px; top: 6px; width: 36px; height: 36px;
    border-radius: 50%; background: #f1ece4;
  }
  .bee-message {
    position: absolute; left: 8px; top: 54px;
    font-family: "Oswald", sans-serif; font-weight: 500;
    font-size: 12px; line-height: 1.35; color: var(--ink);
  }
  .bee-message strong { display: block; font-size: 15px; color: var(--save-red); font-weight: 500; }
  .ingredient-art {
    position: absolute; left: 140px; right: 24px; top: 392px; height: 98px;
    border-radius: 6px;
  }
  .ingredient-art--wildflower {
    background: linear-gradient(180deg, rgba(247,200,96,0.15), rgba(247,200,96,0.55));
  }
  .ingredient-art--saffron {
    background: linear-gradient(90deg, var(--saffron-violet), var(--saffron-red) 45%, var(--saffron-violet));
  }
  .honey-edge {
    position: absolute; left: 0; right: 0; bottom: 0; height: 6px;
    background: linear-gradient(90deg, var(--comb-deep), var(--honey-orange));
  }
</style>
</head>
<body>
<main class="canvas">

  <section class="label label--wildflower">
    <div class="comb-field" role="img" aria-label="Soft honeycomb pattern glow"></div>
    <div class="brand">
      <span class="brand-name">MELVORIN</span>
      <span class="brand-dot"></span>
    </div>
    <div class="product-word">Honey</div>
    <p class="descriptor">Premium<br>honey with a blend of
      <span class="variety variety--wildflower">WILD FLOWER</span>
    </p>
    <div class="bee-badge">
      <svg viewBox="0 0 110 110" width="110" height="110" aria-hidden="true">
        <path d="M2 2 H60 A14 14 0 0 1 74 16 V46 H96 A10 10 0 0 1 106 56 V96 A10 10 0 0 1 96 106 H2" fill="none" stroke="var(--badge-line)" stroke-width="2"/>
      </svg>
      <div class="bee-mark" role="img" aria-label="Small bee line icon"></div>
      <p class="bee-message">Please help us to<strong>SAVE THE BEES</strong></p>
    </div>
    <div class="ingredient-art ingredient-art--wildflower" role="img" aria-label="Golden line illustration of wild flowers"></div>
    <div class="honey-edge"></div>
  </section>

  <section class="label label--saffron">
    <div class="comb-field" role="img" aria-label="Soft honeycomb pattern glow"></div>
    <div class="brand">
      <span class="brand-name">MELVORIN</span>
      <span class="brand-dot"></span>
    </div>
    <div class="product-word">Honey</div>
    <p class="descriptor">Premium<br>honey with a blend of
      <span class="variety variety--saffron">SAFFRON</span>
    </p>
    <div class="bee-badge">
      <svg viewBox="0 0 110 110" width="110" height="110" aria-hidden="true">
        <path d="M2 2 H60 A14 14 0 0 1 74 16 V46 H96 A10 10 0 0 1 106 56 V96 A10 10 0 0 1 96 106 H2" fill="none" stroke="var(--badge-line)" stroke-width="2"/>
      </svg>
      <div class="bee-mark" role="img" aria-label="Small bee line icon"></div>
      <p class="bee-message">Please help us to<strong>SAVE THE BEES</strong></p>
    </div>
    <div class="ingredient-art ingredient-art--saffron" role="img" aria-label="Photo of saffron threads with purple crocus flowers"></div>
    <div class="honey-edge"></div>
  </section>

</main>
</body>
</html>
```